Medical VIP club - small design

Please read the specs in a design brief attached. Also we don't have logo in a Vector format and attaching the only version we have.

Industry/Entity Type

Club

```html
<!DOCTYPE html>
<html lang="en">
<head>
<meta charset="utf-8">
<title>Vitalon VIP Packages</title>
<link rel="stylesheet" href="https://fonts.googleapis.com/css2?family=Ubuntu:wght@300;400;500;700&display=swap">
<style>
  :root {
    --bar-dark: #1e1804;
    --header-brown: #6d5c44;
    --band-dark: #3b2e14;
    --tab-bg: #3e3325;
    --tab-edge: #a39478;
    --tab-text: #f3eedc;
    --panel-cream: #f2f0de;
    --label-light: #ede6c9;
    --label-gold: #cdb07a;
    --ink: #231b08;
    --col-dark: #1d1703;
    --col-mid: #352706;
    --rule: #d9d2b6;
    --gold: #a67d2e;
    --orange: #ec8b18;
    --white: #ffffff;
    --button-text: #c08a2a;
    --phone: #2a2010;
  }
  * { box-sizing: border-box; margin: 0; padding: 0; }
  html, body { width: 1200px; height: 950px; overflow: hidden; }
  body {
    position: relative;
    background: var(--header-brown);
    font-family: "Ubuntu", sans-serif;
  }
  .top-bar { position: absolute; left: 0; top: 0; width: 1200px; height: 17px; background: var(--bar-dark); }
  .hero-band {
    position: absolute; left: 0; top: 110px; width: 1200px; height: 425px;
    background: linear-gradient(180deg, var(--header-brown) 0%, #4c3d22 30%, var(--band-dark) 100%);
  }
  .brand {
    position: absolute; left: 146px; top: 52px;
    display: flex; align-items: center; gap: 10px;
    color: #f2ecd8; font-size: 36px; font-weight: 500;
  }
  .brand-dot { width: 30px; height: 30px; border-radius: 50%; background: #f2ecd8; }
  .phone {
    position: absolute; right: 140px; top: 60px;
    font-size: 29px; font-weight: 300; color: var(--phone); letter-spacing: 1px;
  }
  .nav { position: absolute; top: 132px; left: 0; width: 1200px; height: 42px; }
  .nav a {
    position: absolute; top: 0; height: 42px;
    display: flex; align-items: center; justify-content: center;
    color: var(--tab-text); font-size: 19px; text-decoration: none;
    background: var(--tab-bg);
    border: 1px solid var(--tab-edge); border-bottom: none;
    clip-path: polygon(0 0, calc(100% - 14px) 0, 100% 14px, 100% 100%, 0 100%);
  }
  .panel {
    position: absolute; left: 115px; top: 174px; width: 959px; height: 594px;
    background: var(--panel-cream); border-radius: 0 0 4px 4px;
    box-shadow: 0 4px 12px rgba(0,0,0,0.35); overflow: hidden;
  }
  .panel-title {
    position: absolute; left: 47px; top: 28px;
    font-size: 34px; font-weight: 700; line-height: 32px; color: var(--ink);
  }
  .labels { position: absolute; left: 0; top: 106px; width: 237px; height: 488px;
    background: linear-gradient(100deg, var(--label-light) 0%, #e2d4a8 55%, var(--label-gold) 100%); }
  .label {
    height: 48px; display: flex; align-items: center; justify-content: center;
    font-size: 16px; font-weight: 700; color: var(--ink);
    border-bottom: 1px solid #6b5a3a;
  }
  .pricing-label {
    height: 152px; padding-top: 22px; text-align: center;
    font-size: 28px; font-weight: 500; color: var(--ink);
  }
  .package { position: absolute; top: 48px; width: 240px; height: 546px; }
  .package.dark { background: var(--col-dark); }
  .package.mid { background: var(--col-mid); }
  .package-1 { left: 237px; }
  .package-2 { left: 478px; width: 240px; }
  .package-3 { left: 719px; }
  .package-head {
    height: 58px; display: flex; align-items: center; justify-content: center;
    color: #f4efdc; font-size: 22px; border-bottom: 1px solid var(--rule);
  }
  .package.dark .package-head, .package.mid .package-head { border-radius: 4px 4px 0 0; }
  .feature { height: 48px; display: flex; align-items: center; justify-content: center; border-bottom: 1px solid var(--rule); }
  .feature svg { width: 22px; height: 22px; }
  .price-cell { height: 152px; text-align: center; padding-top: 20px; }
  .price { color: var(--white); font-size: 28px; font-weight: 700; }
  .price .cur { color: var(--orange); }
  .price sup { font-size: 15px; vertical-align: 12px; margin-left: 4px; }
  .select-btn {
    display: inline-flex; align-items: center; justify-content: center;
    margin-top: 17px; width: 172px; height: 57px; border-radius: 4px;
    background: linear-gradient(180deg, #ffffff 0%, #ece8dc 100%);
    color: var(--button-text); font-size: 20px; font-weight: 500;
    border: 1px solid #d8d1bd;
  }
  .col-divider { position: absolute; top: 48px; width: 1px; height: 546px; background: #6a5426; }
  .footer { position: absolute; left: 0; top: 830px; width: 1200px; height: 120px; background: var(--bar-dark); }
  .footer-brand { position: absolute; left: 160px; top: 36px; font-size: 28px; font-weight: 500; color: #4a3f26; }
  .copyright { position: absolute; left: 333px; top: 28px; font-family: Arial, sans-serif; font-size: 12px; color: #f4f0e4; }
  .social { position: absolute; left: 973px; top: 23px; display: flex; gap: 9px; }
  .social span { width: 24px; height: 24px; border-radius: 3px; background: linear-gradient(180deg, #b9b5a2, #6f6b5a); }
</style>
</head>
<body>
  <div class="top-bar"></div>
  <div class="hero-band" role="img" aria-label="Dark damask pattern background"></div>

  <div class="brand"><span class="brand-dot"></span>Vitalon</div>
  <div class="phone">555-010-020</div>

  <nav class="nav">
    <a href="#" style="left:122px;width:97px">Home</a>
    <a href="#" style="left:221px;width:117px">About Us</a>
    <a href="#" style="left:340px;width:111px">VIP Club</a>
    <a href="#" style="left:453px;width:105px">Services</a>
    <a href="#" style="left:560px;width:210px">Packages and Prices</a>
    <a href="#" style="left:772px;width:141px">Registration</a>
    <a href="#" style="left:915px;width:112px">Contacts</a>
  </nav>

  <main class="panel">
    <h1 class="panel-title">Our VIP<br>Packages</h1>

    <div class="labels">
      <div class="label">Option 1</div>
      <div class="label">Option 2</div>
      <div class="label">Option 3</div>
      <div class="label">Option 4</div>
      <div class="label">Option 5</div>
      <div class="label">Option 6</div>
      <div class="label">Option 7</div>
      <div class="pricing-label">Pricing ($)</div>
    </div>

    <section class="package dark package-1">
      <div class="package-head">package 1</div>
      <div class="feature"><svg viewBox="0 0 22 22"><path d="M4 11.5l4.5 4.5L18 6" fill="none" stroke="var(--gold)" stroke-width="3.5" stroke-linecap="round" stroke-linejoin="round"/></svg></div>
      <div class="feature"><svg viewBox="0 0 22 22"><path d="M4 11.5l4.5 4.5L18 6" fill="none" stroke="var(--gold)" stroke-width="3.5" stroke-linecap="round" stroke-linejoin="round"/></svg></div>
      <div class="feature"><svg viewBox="0 0 22 22"><path d="M4 11.5l4.5 4.5L18 6" fill="none" stroke="var(--gold)" stroke-width="3.5" stroke-linecap="round" stroke-linejoin="round"/></svg></div>
      <div class="feature"></div>
      <div class="feature"></div>
      <div class="feature"></div>
      <div class="feature"></div>
      <div class="price-cell">
        <div class="price"><span class="cur">$</span>1000<sup>.00</sup></div>
        <span class="select-btn">Select Option</span>
      </div>
    </section>

    <section class="package mid package-2">
      <div class="package-head">package 2</div>
      <div class="feature"><svg viewBox="0 0 22 22"><path d="M4 11.5l4.5 4.5L18 6" fill="none" stroke="var(--gold)" stroke-width="3.5" stroke-linecap="round" stroke-linejoin="round"/></svg></div>
      <div class="feature"><svg viewBox="0 0 22 22"><path d="M4 11.5l4.5 4.5L18 6" fill="none" stroke="var(--gold)" stroke-width="3.5" stroke-linecap="round" stroke-linejoin="round"/></svg></div>
      <div class="feature"><svg viewBox="0 0 22 22"><path d="M4 11.5l4.5 4.5L18 6" fill="none" stroke="var(--gold)" stroke-width="3.5" stroke-linecap="round" stroke-linejoin="round"/></svg></div>
      <div class="feature"><svg viewBox="0 0 22 22"><path d="M4 11.5l4.5 4.5L18 6" fill="none" stroke="var(--gold)" stroke-width="3.5" stroke-linecap="round" stroke-linejoin="round"/></svg></div>
      <div class="feature"><svg viewBox="0 0 22 22"><path d="M4 11.5l4.5 4.5L18 6" fill="none" stroke="var(--gold)" stroke-width="3.5" stroke-linecap="round" stroke-linejoin="round"/></svg></div>
      <div class="feature"></div>
      <div class="feature"></div>
      <div class="price-cell">
        <div class="price"><span class="cur">$</span>2000<sup>.00</sup></div>
        <span class="select-btn">Select Option</span>
      </div>
    </section>

    <section class="package dark package-3">
      <div class="package-head">package 3</div>
      <div class="feature"><svg viewBox="0 0 22 22"><path d="M4 11.5l4.5 4.5L18 6" fill="none" stroke="var(--gold)" stroke-width="3.5" stroke-linecap="round" stroke-linejoin="round"/></svg></div>
      <div class="feature"><svg viewBox="0 0 22 22"><path d="M4 11.5l4.5 4.5L18 6" fill="none" stroke="var(--gold)" stroke-width="3.5" stroke-linecap="round" stroke-linejoin="round"/></svg></div>
      <div class="feature"><svg viewBox="0 0 22 22"><path d="M4 11.5l4.5 4.5L18 6" fill="none" stroke="var(--gold)" stroke-width="3.5" stroke-linecap="round" stroke-linejoin="round"/></svg></div>
      <div class="feature"><svg viewBox="0 0 22 22"><path d="M4 11.5l4.5 4.5L18 6" fill="none" stroke="var(--gold)" stroke-width="3.5" stroke-linecap="round" stroke-linejoin="round"/></svg></div>
      <div class="feature"><svg viewBox="0 0 22 22"><path d="M4 11.5l4.5 4.5L18 6" fill="none" stroke="var(--gold)" stroke-width="3.5" stroke-linecap="round" stroke-linejoin="round"/></svg></div>
      <div class="feature"><svg viewBox="0 0 22 22"><path d="M4 11.5l4.5 4.5L18 6" fill="none" stroke="var(--gold)" stroke-width="3.5" stroke-linecap="round" stroke-linejoin="round"/></svg></div>
      <div class="feature"><svg viewBox="0 0 22 22"><path d="M4 11.5l4.5 4.5L18 6" fill="none" stroke="var(--gold)" stroke-width="3.5" stroke-linecap="round" stroke-linejoin="round"/></svg></div>
      <div class="price-cell">
        <div class="price"><span class="cur">$</span>3000<sup>.00</sup></div>
        <span class="select-btn">Select Option</span>
      </div>
    </section>

    <div class="col-divider" style="left:477px"></div>
    <div class="col-divider" style="left:718px"></div>
  </main>

  <footer class="footer">
    <div class="footer-brand">Vitalon</div>
    <p class="copyright">Copyright 2010 Vitalon. All rights reserved.</p>
    <div class="social" aria-label="Social links">
      <span></span><span></span><span></span>
    </div>
  </footer>
</body>
</html>
```